Business Card for Inovative Flexible Packaging Company

Create a business card that is both simple and stricking at the same time.
Preferably only one color (orange) or two colors (black and orange).
Information to print:
Corvela, Lda
[T] 22 418 6093
[M] 91 362 7148
[F] 22 418 6057
[@] corvela.mt@tarnomail.example
SEDE & ARMAZÉM
Rua Dos Vimieiros do Outeiro, 317
Serzedo
4410-862 Serzedo - VN Gaia
PORTUGAL
Reason: A lot of the ideas are obvious. I want something different. Inovative. dare to do something eye catching with style.
Business Consumers. Packaging Designers.
Business

```html
<!DOCTYPE html>
<html lang="pt">
<head>
<meta charset="utf-8">
<title>Corvela, Lda — Cartão de visita</title>
<link href="https://fonts.googleapis.com/css2?family=Open+Sans:wght@400;600&display=swap" rel="stylesheet">
<style>
  :root {
    --page-bg: #2a1d15;
    --card-black: #050505;
    --card-glow: #2b2b2b;
    --band-dark: #0b0b0b;
    --band-line: #3a3a3a;
    --brand-orange: #f26a1b;
    --accent-orange: #c4520f;
    --text-light: #f2f2f2;
    --text-muted: #c8c8c8;
  }
  * { margin: 0; padding: 0; box-sizing: border-box; }
  html, body {
    width: 1200px; height: 750px; overflow: hidden;
    background: var(--page-bg);
    font-family: "Open Sans", Arial, sans-serif;
  }
  .canvas { position: relative; width: 1200px; height: 750px; }
  .card {
    position: absolute; top: 211px;
    width: 545px; height: 283px;
    background: var(--card-black);
    overflow: hidden;
    box-shadow: 0 4px 14px rgba(0,0,0,0.55);
  }
  .card--front { left: 58px; }
  .card--back { left: 622px; }
  .card__texture {
    position: absolute; inset: 0;
    background: radial-gradient(ellipse 60% 70% at 50% 35%, var(--card-glow) 0%, #141414 50%, var(--card-black) 100%);
  }
  .card--back .card__texture {
    background: radial-gradient(ellipse 55% 55% at 45% 25%, #262626 0%, #111 55%, var(--card-black) 100%);
  }
  .brand {
    position: absolute; left: 0; right: 0; top: 110px;
    display: flex; align-items: center; justify-content: center; gap: 14px;
  }
  .brand__mark {
    width: 22px; height: 22px;
    background: var(--brand-orange);
  }
  .brand__name {
    font-size: 46px; font-weight: 400; line-height: 1;
    color: var(--text-light);
    letter-spacing: 1px;
  }
  .card__accents { position: absolute; inset: 0; }
  .office-band {
    position: absolute; left: 0; right: 0; top: 111px; height: 49px;
    background: var(--band-dark);
    border-top: 2px solid var(--band-line);
    border-bottom: 2px solid var(--band-line);
    display: flex; align-items: center; justify-content: center;
  }
  .office-band__title {
    font-size: 27px; font-weight: 400; color: var(--text-light);
    letter-spacing: 0.5px;
  }
  .contact {
    position: absolute; left: 52px; top: 170px;
    font-size: 14.5px; line-height: 21.5px;
    color: var(--text-light);
    list-style: none;
  }
  .contact__phones span { margin-right: 18px; }
  .contact__phones span:last-child { margin-right: 0; }
</style>
</head>
<body>
<main class="canvas">
  <section class="card card--front" aria-label="Frente do cartão">
    <div class="card__texture" role="img" aria-label="Textura escura com padrão geométrico discreto"></div>
    <div class="brand">
      <span class="brand__mark" aria-hidden="true"></span>
      <span class="brand__name">Corvela</span>
    </div>
  </section>

  <section class="card card--back" aria-label="Verso do cartão">
    <div class="card__texture" role="img" aria-label="Textura escura com padrão geométrico discreto"></div>
    <svg class="card__accents" width="545" height="283" viewBox="0 0 545 283" aria-hidden="true">
      <polygon points="20,0 180,0 205,111 0,111 0,40" fill="var(--accent-orange)" opacity="0.1"/>
      <polygon points="320,0 545,0 545,111 400,111" fill="var(--accent-orange)" opacity="0.12"/>
      <polygon points="430,160 545,160 545,283 520,283" fill="var(--accent-orange)" opacity="0.08"/>
    </svg>
    <div class="office-band">
      <h2 class="office-band__title">SEDE &amp; ARMAZÉM</h2>
    </div>
    <ul class="contact">
      <li>Rua Dos Vimieiros do Outeiro, 317 Serzedo</li>
      <li>4410-862 Serzedo - VN Gaia PORTUGAL</li>
      <li>corvela.mt@tarnomail.example</li>
      <li class="contact__phones"><span>t. 22 418 6093</span><span>m. 91 362 7148</span><span>f. 22 418 6057</span></li>
    </ul>
  </section>
</main>
</body>
</html>
```